Zestora - The Natural Energydrink
Zielgruppe
Wir sind eine Imkerei und unsere Zielgruppe ist der Moderne verbraucher der auf die umwelt achtet und sich bewusst ernähren möchte. Zielgruppe ist von 16-33 Jahren ca.
Aufgabenstellung
Es geht um Zestora, ein Natural Energydrink der in einer 0,33l Limonadenflasche abgefüllt werden soll und nicht in eine Dose, das ist auch schon der gedanke hinter dem Produkt. Natürlichkeit, Umweltbewusstsein, Ökologisch. Der Energydrink, der ausschließlich mit Honig gesüßt ist und nicht mit Industriellen Zucker. Das Etikett für den Natural Energydrink soll Modern sein aber auch die 'Ältere' zielgruppe ansprechen. Gewünscht ist ein Front, Rücken und Hals Etikett für die Flasche die auch gut zusammen passen. Rücken ist dann natürlich fast nur inhaltstoffe und hersteller und eben diese Pflichtangaben.
Das Thema Biene und Honig sollte sich natürlich wiederfinden und das Design sollte in Gelb schwarz gehalten sein. Auch Wabenmuster machen sich gut. Nicht zu 'lieb' es ist immerhin noch ein energy drink aber auch nicht zu 'Hart' es soll auch die naturverliebten 'Ökos' ansprechen. Schwieriger Spagat zwischen Öko und Energydrink in berücksichtigung der Honig Thematik.
Maße können die klassischen 0,33l Etikettenmaße sein, müssen sie aber nicht.
Front: 9cm hoch und 8,5cm breit
Halsetikett: 6cm hoch und 9cm breit mit Überlappung
Rücken Etikett: 8cm hoch und 6cm breit
Größe und Form sind aber nicht vorgegeben. Es sollte am schluss harmonisch sein und gut und übersichtlich alle Informationen griffbereit sein für den verbraucher.
Pflichtangaben auf dem Rückenetikett sind:
die Zutaten auflistung und die klassische Tabelle auf 100ml und auf 0,33ml ( Zucker, Kcal usw.) Es sollte ein EAN Code mit eingebunden werden und solche dinge wie ein Facebook und Instagram Symbol machen sich auch immer gut. Weiterhin der Textblock: 'Kohlensäurehaltig, Koffeinhaltig, kühl und trocken lagern. Für Kinder, Diabetiker, schwangere Frauen und koffeinempfindliche Personen nicht geeignet. Nur in Begrensten Mengen Konsumieren.'
Darüber hinaus muss natürlich der sehr werbewirksame Slogan ' Made in Germany' dazu ;)

```html
<!DOCTYPE html>
<html lang="de">
<head>
<meta charset="utf-8">
<title>Zestora – Halsetikett</title>
<link rel="stylesheet" href="https://fonts.googleapis.com/css2?family=Lilita+One&display=swap">
<style>
  :root {
    --canvas: #ffffff;
    --label-black: #0c0c0c;
    --comb-black: #141414;
    --honey: #f6c20f;
    --honey-light: #fbe14a;
    --honey-deep: #e8ac05;
    --band-yellow: #fecb00;
  }
  html, body {
    margin: 0;
    padding: 0;
    width: 1200px;
    height: 636px;
    overflow: hidden;
    background: var(--canvas);
  }
  .neck-label {
    position: relative;
    width: 1200px;
    height: 636px;
  }
  .neck-label__art {
    position: absolute;
    inset: 0;
    display: block;
  }
  .brand-name {
    position: absolute;
    left: 600px;
    top: 318px;
    transform: translate(-50%, -50%) rotate(90deg);
    margin: 0;
    font-family: "Lilita One", "Arial Black", sans-serif;
    font-weight: 400;
    font-size: 74px;
    letter-spacing: 4px;
    line-height: 1;
    color: var(--honey);
    white-space: nowrap;
  }
</style>
</head>
<body>
  <main class="neck-label">
    <svg class="neck-label__art" viewBox="0 0 1200 636" width="1200" height="636" aria-hidden="false">
      <defs>
        <clipPath id="label-shape">
          <polygon points="145,0 1057,0 1200,636 0,636"/>
        </clipPath>
        <linearGradient id="honey-fill" x1="0" y1="0" x2="0" y2="1">
          <stop offset="0" stop-color="var(--honey-light)"/>
          <stop offset="0.55" stop-color="var(--honey)"/>
          <stop offset="1" stop-color="var(--honey-deep)"/>
        </linearGradient>
      </defs>
      <g clip-path="url(#label-shape)">
        <rect class="label-base" x="0" y="0" width="1200" height="636" fill="var(--label-black)"/>
        <rect class="honeycomb-area" x="0" y="120" width="1200" height="489" fill="var(--comb-black)"
              role="img" aria-label="Dunkles Wabenmuster aus Sechsecken über die ganze Fläche"/>
        <rect class="honey-drip-area" x="0" y="0" width="1200" height="120" fill="url(#honey-fill)"
              role="img" aria-label="Herabtropfender Honig entlang der Oberkante"/>
        <rect class="bottom-band" x="0" y="609" width="1200" height="27" fill="var(--band-yellow)"/>
      </g>
      <circle class="bee-mark" cx="597" cy="556" r="16" fill="var(--honey)"
              role="img" aria-label="Kleines Bienensymbol"/>
    </svg>
    <h1 class="brand-name">ZESTORA</h1>
  </main>
</body>
</html>
```